Bookcover: Lessons From the Silent Orchard

I am publishing a super-low-cost innovation book for €4,99 on Bravolo Self Release to help everyone become a great innovator: young ambitious people without college education nor a big budget. Do you want to help me?

Brief:
Design a book cover 1600 x 2560 pixels for BSR.
Main title: Lessons From the Silent Orchard
Sub title: mindset - insights - skills & tools
Author: Maarten de Klerk
Design: captive, and appealing to everyone
Target Group: young ambitious people without college education

For bravolo please format the height/width ratio of 1.6:1

```html
<!DOCTYPE html>
<html lang="en">
<head>
<meta charset="UTF-8">
<title>Lessons From the Silent Orchard — Book Cover</title>
<link rel="stylesheet" href="https://fonts.googleapis.com/css2?family=Bebas+Neue&family=Antonio:wght@100&display=swap">
<style>
  :root {
    --page-bg: #ffffff;
    --cover-orange: #fd8c03;
    --ink: #000000;
    --band-dark: #231f20;
    --author-white: #ffffff;
    --bulb-yellow: #f3c93a;
    --bulb-deep: #d9a81e;
  }
  html, body {
    margin: 0;
    padding: 0;
    width: 1200px;
    height: 1200px;
    overflow: hidden;
    background: var(--page-bg);
  }
  .canvas {
    position: relative;
    width: 1200px;
    height: 1200px;
  }
  .cover {
    position: absolute;
    left: 295px;
    top: 141px;
    width: 618px;
    height: 925px;
    background: var(--cover-orange);
    overflow: hidden;
  }
  .title-line {
    position: absolute;
    left: 33px;
    margin: 0;
    font-family: "Bebas Neue", sans-serif;
    font-weight: 400;
    line-height: 1;
    color: var(--ink);
    white-space: nowrap;
  }
  .title-line--lessons { top: 31px; font-size: 157px; }
  .title-line--from { top: 153px; font-size: 157px; }
  .title-line--silent {
    top: 283px;
    font-size: 195px;
    display: flex;
    align-items: flex-start;
    gap: 14px;
  }
  .title-line--orchard { top: 453px; font-size: 157px; }
  .idea-bulb {
    width: 118px;
    height: 150px;
    margin-top: 18px;
    border-radius: 50% 50% 30% 30% / 55% 55% 25% 25%;
    background: radial-gradient(circle at 45% 38%, var(--bulb-yellow), var(--bulb-deep));
    flex: none;
  }
  .subtitle {
    position: absolute;
    left: 33px;
    top: 612px;
    margin: 0;
    font-family: "Antonio", sans-serif;
    font-weight: 100;
    font-size: 80px;
    line-height: 75px;
    color: var(--ink);
    text-transform: uppercase;
  }
  .author-band {
    position: absolute;
    left: 0;
    bottom: 0;
    width: 100%;
    height: 116px;
    background: var(--band-dark);
  }
  .author-name {
    position: absolute;
    left: 33px;
    top: 42px;
    margin: 0;
    font-family: "Bebas Neue", sans-serif;
    font-weight: 400;
    font-size: 53px;
    line-height: 1;
    color: var(--author-white);
    white-space: nowrap;
  }
</style>
</head>
<body>
  <div class="canvas">
    <article class="cover">
      <h1 class="book-title">
        <span class="title-line title-line--lessons">Lessons</span>
        <span class="title-line title-line--from">From the</span>
        <span class="title-line title-line--silent">Silent<span class="idea-bulb" role="img" aria-label="Illustration of a crumpled yellow paper light bulb with glowing rays"></span></span>
        <span class="title-line title-line--orchard">Orchard</span>
      </h1>
      <p class="subtitle">Mindset - Insights -<br>Skills &amp; Tools</p>
      <footer class="author-band">
        <p class="author-name">MAARTEN DE KLERK</p>
      </footer>
    </article>
  </div>
</body>
</html>
```